Business Cards for an 'affordable luxury' inner city home builder in Calgary.

We need a business card design that emulates the progressive, innovative, culture of our company and the modern style of our homes. Use our website www.velmarcrest-ab.com as a reference for the product we build.

Our company builds homes in the inner city space of Calgary, Alberta. We build affordable luxury.

Target Market(s)

Young professional Families

Contact Information for Business Card

Try to maintain consistency with the logo font and the card font.

Requirements
Must have
• The details must include: Name, education, title, phone number, website and email (Address is not as important)
• The design must be uniques (like our logo), elegant, sophisticated and modern.

```html
<!DOCTYPE html>
<html lang="en">
<head>
<meta charset="utf-8">
<title>Velmarcrest Homes Ltd — Business Cards</title>
<link href="https://fonts.googleapis.com/css2?family=Montserrat:wght@500;700&family=Roboto:wght@400&display=swap" rel="stylesheet">
<style>
  :root {
    --backdrop: #1c1c1c;
    --card-dark: #242424;
    --card-light: #ffffff;
    --ink: #2a2a2a;
    --muted: #8a8a8a;
    --on-dark: #ffffff;
  }
  * { box-sizing: border-box; margin: 0; padding: 0; }
  html, body { width: 1200px; height: 900px; overflow: hidden; }
  body {
    background: var(--backdrop);
    font-family: "Montserrat", sans-serif;
    position: relative;
  }
  .card {
    position: absolute;
    width: 525px;
    height: 300px;
    border-radius: 14px;
    overflow: hidden;
    box-shadow: 0 18px 40px rgba(0,0,0,0.55);
  }
  .card--back {
    left: 70px;
    top: 110px;
    background: var(--card-dark);
  }
  .card--front {
    left: 605px;
    top: 490px;
    background: var(--card-light);
  }
  .wordmark {
    display: flex;
    align-items: center;
    gap: 16px;
    color: var(--on-dark);
    font-weight: 500;
    text-transform: uppercase;
    letter-spacing: 1.5px;
    line-height: 1.02;
  }
  .wordmark__square {
    width: 44px;
    height: 44px;
    border: 3px solid var(--on-dark);
    flex: none;
  }
  .card--back .wordmark {
    position: absolute;
    left: 120px;
    top: 104px;
    font-size: 27px;
  }
  .front__band {
    position: absolute;
    inset: 0;
    width: 100%;
    height: 100%;
  }
  .card--front .wordmark {
    position: absolute;
    left: 34px;
    top: 40px;
    font-size: 22px;
  }
  .person {
    position: absolute;
    left: 34px;
    bottom: 44px;
  }
  .person__name {
    font-size: 25px;
    font-weight: 700;
    color: var(--ink);
  }
  .person__title {
    margin-top: 6px;
    font-size: 15px;
    font-weight: 500;
    color: var(--muted);
  }
  .contact {
    position: absolute;
    left: 300px;
    top: 150px;
    list-style: none;
    font-family: "Roboto", sans-serif;
    font-size: 12.5px;
    color: var(--muted);
    line-height: 1.55;
  }
  .contact li { display: flex; align-items: center; gap: 7px; }
  .contact__address { padding-left: 0; margin-bottom: 2px; }
  .contact svg { width: 11px; height: 11px; fill: var(--ink); flex: none; }
</style>
</head>
<body>

  <section class="card card--back" aria-label="Card back">
    <div class="wordmark">
      <span class="wordmark__square"></span>
      <span>Velmarcrest<br>Homes Ltd</span>
    </div>
  </section>

  <section class="card card--front" aria-label="Card front">
    <svg class="front__band" viewBox="0 0 525 300" preserveAspectRatio="none" aria-hidden="true">
      <polygon points="0,0 525,0 525,95 320,95 300,128 0,128" fill="var(--card-dark)"/>
    </svg>

    <div class="wordmark">
      <span>Velmarcrest<br>Homes Ltd</span>
    </div>

    <div class="person">
      <p class="person__name">Aldric Norwood</p>
      <p class="person__title">Director</p>
    </div>

    <ul class="contact">
      <li class="contact__address">482 17 Ave NE Calgary, AB</li>
      <li>
        <svg viewBox="0 0 24 24"><path d="M6.6 10.8a15 15 0 0 0 6.6 6.6l2.2-2.2c.3-.3.7-.4 1-.2 1.1.4 2.3.6 3.6.6.6 0 1 .4 1 1V20c0 .6-.4 1-1 1A17 17 0 0 1 3 4c0-.6.4-1 1-1h3.5c.6 0 1 .4 1 1 0 1.3.2 2.5.6 3.6.1.3 0 .7-.2 1z"/></svg>
        403-555-0148
      </li>
      <li>
        <svg viewBox="0 0 24 24"><path d="M7 1h10a2 2 0 0 1 2 2v18a2 2 0 0 1-2 2H7a2 2 0 0 1-2-2V3a2 2 0 0 1 2-2zm0 3v14h10V4zm5 15.5a1 1 0 1 0 0 2 1 1 0 0 0 0-2z"/></svg>
        8500 555 210
      </li>
      <li>
        <svg viewBox="0 0 24 24"><path d="M2 5h20v14H2zm2 2v.5l8 5 8-5V7zm0 2.8V17h16V9.8l-8 5z"/></svg>
        projects@velmarcrest-ab.com
      </li>
      <li>
        <svg viewBox="0 0 24 24"><path d="M12 2a10 10 0 1 0 0 20 10 10 0 0 0 0-20zm6.9 6h-2.9a15 15 0 0 0-1.4-3.6A8 8 0 0 1 18.9 8zM12 4c.8 1.2 1.5 2.5 1.9 4h-3.8c.4-1.5 1.1-2.8 1.9-4zM4.3 14a8 8 0 0 1 0-4h3.4a16 16 0 0 0 0 4zm.8 2h2.9c.3 1.3.8 2.5 1.4 3.6A8 8 0 0 1 5.1 16zM8 8H5.1a8 8 0 0 1 4.3-3.6C8.8 5.5 8.3 6.7 8 8zm4 12c-.8-1.2-1.5-2.5-1.9-4h3.8c-.4 1.5-1.1 2.8-1.9 4zm2.3-6H9.7a14 14 0 0 1 0-4h4.6a14 14 0 0 1 0 4zm.3 5.6c.6-1.1 1.1-2.3 1.4-3.6h2.9a8 8 0 0 1-4.3 3.6zm1.7-5.6a16 16 0 0 0 0-4h3.4a8 8 0 0 1 0 4z"/></svg>
        www.velmarcrest-ab.com
      </li>
    </ul>
  </section>

</body>
</html>
```